Zielgruppe
Die travlon GmbH bietet professionelle Cloud-Lösungen im Bereich spezialisierter Verwaltungssysteme. Hierbei handelt es sich um Software as a Service (SaaS), die zu 100% von der travlon GmbH betrieben und kontinuierlich weiterentwickelt wird.
Aufgabenstellung
Das Design kann Farben und/oder Elemente der travlon GmbH enthalten (www.travlon.de). Da es sich um ein eigenen Produkt handelt, muss jedoch auch Neutralität bewahrt werden.

```html
<!DOCTYPE html>
<html lang="de">
<head>
<meta charset="utf-8">
<title>Anmeldung</title>
<link rel="stylesheet" href="https://fonts.googleapis.com/css2?family=Lato:wght@400;700&display=swap">
<style>
  :root {
    --bg-light: #b9c3cb;
    --bg-mid: #8c9dab;
    --bg-dark: #4a6079;
    --accent-red: #d0043c;
    --card: #ffffff;
    --frame: #cfd3d7;
    --text: #4a5560;
    --muted: #6f8291;
    --field-bg: #f2f2f2;
    --field-border: #c9cdd1;
  }
  * { box-sizing: border-box; margin: 0; padding: 0; }
  html, body { width: 1200px; height: 731px; overflow: hidden; }
  body {
    position: relative;
    font-family: "Lato", sans-serif;
    color: var(--text);
  }
  .backdrop {
    position: absolute; inset: 0;
    background: linear-gradient(100deg, var(--bg-light) 0%, var(--bg-mid) 45%, var(--bg-dark) 100%);
  }
  .login-card {
    position: absolute; left: 305px; top: 216px; width: 590px; height: 283px;
    background: var(--card); border-radius: 4px;
    box-shadow: 0 2px 8px rgba(0,0,0,0.12);
  }
  .login-frame {
    position: absolute; left: 30px; top: 42px; width: 530px; height: 195px;
    border: 1px solid var(--frame); border-radius: 2px;
  }
  .login-legend {
    position: absolute; left: 18px; top: -11px; padding: 0 11px;
    background: var(--card); font-size: 13.5px; line-height: 20px; color: var(--text);
  }
  .field-label { position: absolute; left: 58px; font-size: 11.5px; line-height: 14px; }
  .field-input {
    position: absolute; left: 170px; width: 248px; height: 26px;
    border: 1px solid var(--field-border); border-radius: 13px;
    background: var(--field-bg); font-size: 10.5px;
    color: #6a6f74; padding: 0 17px; line-height: 24px;
  }
  .password-dots { letter-spacing: 1.5px; font-size: 8px; }
  .toggle-visibility { position: absolute; left: 425px; }
  .submit-button {
    position: absolute; left: 172px; top: 116px; width: 115px; height: 25px;
    border-radius: 13px; background: var(--accent-red); color: #fff;
    font-weight: 700; font-size: 11px; text-align: center; line-height: 25px;
  }
  .forgot-link {
    position: absolute; right: 32px; top: 246px; font-size: 11.5px;
    color: var(--muted); text-decoration: none;
  }
</style>
</head>
<body>
  <div class="backdrop" role="img" aria-label="Dekorativer Hintergrund mit geschwungenen Farbbändern in Rot, Hellblau und Sand auf graublauem Verlauf"></div>

  <main class="login-card">
    <section class="login-frame">
      <span class="login-legend">Anmeldebereich</span>
      <span class="field-label" style="top:51px">Benutzername:</span>
      <span class="field-input" style="top:45px">Loginseite</span>
      <span class="field-label" style="top:84px">Passwort:</span>
      <span class="field-input password-dots" style="top:77px">●●●●●●●●●●●</span>
      <svg class="toggle-visibility" style="top:84px" width="17" height="12" viewBox="0 0 17 12" aria-label="Passwort anzeigen">
        <path d="M1 6 Q8.5 -2 16 6 Q8.5 14 1 6 Z" fill="none" stroke="#555" stroke-width="1.2"/>
        <circle cx="8.5" cy="6" r="3" fill="none" stroke="#555" stroke-width="1.2"/>
        <circle cx="8.5" cy="6" r="1.6" fill="#555"/>
      </svg>
      <span class="submit-button">Anmelden</span>
    </section>
    <a class="forgot-link" href="#">Passwort vergessen?</a>
  </main>
</body>
</html>
```